Flyer-Design für Yoga-Studio
Zielgruppe
Yoga-Studio, Zielgruppe: alle Erwachsenen
Aufgabenstellung
Der Flyer soll nicht feminin wirken, eher in Grau-Blau oder Braun Tönen. Nicht überladen oder verschnörkelt. Es darf gerne ein Symbol darin vorkommen. Gerne DinA6 (Hinter und Forderseite)
Der Flyer ist für die Neueröffnung eines Yogastudios, alle wichtigen Infos sollen enthalten sein.

```html
<!DOCTYPE html>
<html lang="de">
<head>
<meta charset="utf-8">
<title>Sattva Yoga – Flyer Vorder- und Rückseite</title>
<link href="https://fonts.googleapis.com/css2?family=Kalam:wght@700&family=Lato:wght@400;700;900&family=Open+Sans:wght@400;600;700&display=swap" rel="stylesheet">
<style>
  :root{
    --page:#ffffff;
    --maroon:#3a0503;
    --maroon-banner:#4a0c05;
    --brown-text:#5a1c08;
    --gold:#f5c34a;
    --gold-deep:#e8a232;
    --ochre:#f0b51e;
    --cream:#fff6e4;
    --sun-1:#ffd35a;
    --sun-2:#f7962a;
    --sun-3:#d8521a;
    --warm-1:#fbe24a;
    --warm-2:#f2c43a;
    --warm-3:#e2902a;
    --warm-4:#c25a1a;
    --ember:#b4501a;
  }
  *{margin:0;padding:0;box-sizing:border-box}
  html,body{width:1200px;height:865px;overflow:hidden;background:var(--page)}
  body{position:relative;font-family:"Open Sans",Arial,sans-serif}

  .flyer{position:absolute;top:65px;width:530px;height:746px;overflow:hidden}
  .flyer--front{left:58px;background:var(--maroon)}
  .flyer--back{left:615px}

  .line{position:absolute;left:0;right:0;text-align:center;white-space:nowrap}

  /* front */
  .sunrise-photo{position:absolute;left:0;top:0;width:100%;height:400px;
    background:linear-gradient(180deg,var(--sun-1) 0%,var(--sun-2) 35%,var(--sun-3) 65%,var(--maroon) 100%)}
  .front-name{position:absolute;right:40px;top:60px;width:190px;height:150px;display:flex;align-items:center;justify-content:center;
    font-family:"Lato",sans-serif;font-weight:900;font-size:22px;color:#4a3a30;letter-spacing:1px}
  .front-brand{position:absolute;right:38px;top:205px;text-align:right;color:var(--maroon)}
  .front-brand .brand{font-family:"Lato",sans-serif;font-weight:900;font-size:20px;line-height:26px;color:#2a0a05}
  .front-brand .style{font-family:"Open Sans",sans-serif;font-size:14.5px;line-height:25px}
  .headline{top:375px;font-family:"Kalam",cursive;font-weight:700;font-size:62px;line-height:80px;color:var(--gold)}
  .tagline{font-size:15px;line-height:24px;color:var(--cream)}
  .rule{position:absolute;left:110px;width:310px;height:1px;background:var(--gold-deep)}
  .days{font-weight:700;font-size:16px;color:var(--cream)}
  .time{font-size:20px;color:var(--cream)}
  .ask{font-weight:700;font-size:16px;color:var(--gold-deep)}
  .contact{font-size:15px;line-height:23px;color:var(--cream)}
  .contact b{font-weight:700}
  .follow{font-size:11.5px;letter-spacing:3px;color:var(--cream);display:flex;justify-content:center;align-items:center;gap:8px}
  .follow .sep{width:1px;height:18px;background:var(--gold-deep)}
  .follow .dot{width:12px;height:12px;background:var(--cream)}
  .follow .handle{font-weight:700;letter-spacing:0;font-size:14px}
  .address{font-size:14px;color:var(--gold)}

  /* back */
  .meditation-photo{position:absolute;inset:0;
    background:
      linear-gradient(180deg,rgba(194,90,26,0) 55%,rgba(200,104,26,.85) 80%,var(--ember) 100%),
      radial-gradient(ellipse at 50% 35%,var(--warm-1) 0%,var(--warm-2) 45%,var(--warm-3) 80%,var(--warm-4) 100%)}
  .top-banner{position:absolute;left:51px;top:0;width:449px;height:52px;background:var(--maroon-banner);
    clip-path:polygon(0 0,100% 0,92% 100%,8% 100%);display:flex;align-items:center;justify-content:center;
    font-family:"Lato",sans-serif;font-weight:900;font-size:19px;color:var(--ochre)}
  .back-name{position:absolute;left:165px;top:80px;width:200px;height:160px;display:flex;align-items:center;justify-content:center;
    font-family:"Lato",sans-serif;font-weight:900;font-size:22px;color:#4a3a30;letter-spacing:1px}
  .class-title{font-family:"Lato",sans-serif;font-weight:700;font-size:30px;line-height:36px;color:var(--brown-text)}
  .class-time{font-family:"Lato",sans-serif;font-size:15px;line-height:20px;color:var(--brown-text)}
  .class-time b{font-weight:700}
  .free-banner{position:absolute;left:51px;top:481px;width:431px;height:98px;background:var(--maroon-banner);
    clip-path:polygon(4% 0,96% 0,100% 50%,96% 100%,4% 100%,0 50%)}
  .free-title{top:488px;font-family:"Lato",sans-serif;font-weight:900;font-size:30px;line-height:36px;letter-spacing:4px;color:var(--cream)}
  .free-sub{font-family:"Lato",sans-serif;font-size:15px;color:var(--cream)}
  .free-when{font-family:"Lato",sans-serif;font-size:17px;color:var(--cream)}
  .free-when b{font-weight:700}
  .flyer--back .contact{color:var(--cream)}
  .flyer--back .ask{color:var(--gold)}
  .flyer--back .address{color:var(--gold)}
</style>
</head>
<body>

<section class="flyer flyer--front">
  <div class="sunrise-photo" role="img" aria-label="Foto: Silhouette einer Person in Yoga-Pose vor orangem Sonnenaufgang"></div>
  <div class="front-name">SATTVA YOGA</div>
  <div class="front-brand">
    <div class="brand">SATTVA YOGA</div>
    <div class="style">HATHA YOGA</div>
    <div class="style">ASHTANGA YOGA</div>
    <div class="style">PRANAJAMAS</div>
  </div>
  <h1 class="line headline">Morgen Yoga</h1>
  <p class="line tagline" style="top:472px">WACH • ENERGIEGELADEN •</p>
  <p class="line tagline" style="top:496px">AUSGEGLICHEN IN DEN TAG STARTEN</p>
  <div class="rule" style="top:530px"></div>
  <p class="line days" style="top:535px">Montag bis Freitag</p>
  <p class="line time" style="top:558px">6.45-7.45 Uhr</p>
  <div class="rule" style="top:588px"></div>
  <p class="line ask" style="top:596px">Interessiert?</p>
  <p class="line contact" style="top:617px">Anmeldungen oder Fragen (auch Probelektionen)</p>
  <p class="line contact" style="top:640px">Whatsapp an Lukas <b>076 000 12 34</b></p>
  <div class="line follow" style="top:685px"><span>FOLLOW US ON</span><span class="sep"></span><span class="dot"></span><span class="sep"></span><span class="handle">SATTVAYOGA</span></div>
  <p class="line address" style="top:706px">Lindenweg 7, 1234 Musterstadt</p>
</section>

<section class="flyer flyer--back">
  <div class="meditation-photo" role="img" aria-label="Foto: unscharfe Person in Meditationshaltung in warmem Gelblicht"></div>
  <div class="top-banner">SATTVA YOGA</div>
  <div class="back-name">SATTVA YOGA</div>
  <h2 class="line class-title" style="top:245px">Hatha Yoga</h2>
  <p class="line class-time" style="top:284px"><b>Montag bis Freitag-</b> 6.45-7.45 Uhr</p>
  <h2 class="line class-title" style="top:318px">Pranajamas</h2>
  <p class="line class-time" style="top:355px"><b>Auf Anfrage</b></p>
  <h2 class="line class-title" style="top:383px">Ashtanga Yoga</h2>
  <p class="line class-time" style="top:424px"><b>Montag, Dienstag und Donnerstag</b> - 8.30 - 10.00 Uhr</p>
  <div class="free-banner"></div>
  <h2 class="line free-title">GRATIS YOGA</h2>
  <p class="line free-sub" style="top:520px">Hatha oder Ashtanga</p>
  <p class="line free-when" style="top:541px"><b>Jeden Mittwoch</b> -17-18.30 Uhr</p>
  <p class="line ask" style="top:596px">Interessiert?</p>
  <p class="line contact" style="top:617px">Anmeldungen oder Fragen (auch Probelektionen)</p>
  <p class="line contact" style="top:640px">Whatsapp an Lukas <b>076 000 12 34</b></p>
  <div class="line follow" style="top:685px"><span>FOLLOW US ON</span><span class="sep"></span><span class="dot"></span><span class="sep"></span><span class="handle">SATTVAYOGA</span></div>
  <p class="line address" style="top:706px">Lindenweg 7, 1234 Musterstadt</p>
</section>

</body>
</html>
```